Flyer for Encounter G.L.O. - Hour of Glory!

We are producing a monthly Hour of Glory that supports local Christian Contemporary artists and raises money for charities. We are looking for a flyer design for our flyers, posters, and postcards (some mailed and some handed out). We want to create a modern and impressive flyer that will capture audiences.

Event details -
Tag: experience the night. praise the night.
A Hour of Glory you will not want to miss
Let's worship! Live band covering your favorite popular contemporary Christian music! All ages welcome!
Date: Wednesday, May 27th, 2015
7:00 pm to 8:15 pm
Location: The Harborview Chapel
2715 W Maple Crest Rd; Fort Lauderdale, FL 33918

Event is FREE!! Please bring a donation of gently used clothing items or new toiletry item.
Benefit for: The Open Hands Mission

This month's debut artist: Talia Verhoeven - local Christian Singer/Songwriter.

for more details, visit: www.encounterpraiseGLO.example
brought to you by: Delphine Marsh Music
___
Please see our website for style of what we are looking for. Also attached is a template design that I like and would love to see if we can do something like this.

Target Market(s)

all ages - young, older, modern, contemporary - youth

Industry/Entity Type

Artists

Colors
ec1f27
6b449b
ffffff

Requirements
Must have
• Cool design, bring a new "vibe" to Christian music -
• Black design
• worship photos like in the attached template ideas.

```html
<!DOCTYPE html>
<html lang="en">
<head>
<meta charset="utf-8">
<title>Encounter G.L.O. – Hour of Glory</title>
<link href="https://fonts.googleapis.com/css2?family=Bebas+Neue&family=Oswald:wght@400;500;600;700&family=Cinzel:wght@600&display=swap" rel="stylesheet">
<style>
  :root {
    --ink: #07040d;
    --night: #150a26;
    --violet: #6b449b;
    --glow: #9b5cff;
    --lavender: #ecd4ff;
    --pink: #ff3d8b;
    --red: #ec1f27;
    --white: #ffffff;
    --slate: #4a4d52;
  }
  * { margin: 0; padding: 0; box-sizing: border-box; }
  html, body { width: 835px; height: 1200px; overflow: hidden; background: var(--ink); }
  .flyer {
    position: relative; width: 835px; height: 1200px; overflow: hidden;
    background:
      radial-gradient(ellipse 45% 18% at 62% 78%, rgba(155,92,255,.35), transparent 70%),
      radial-gradient(ellipse 70% 25% at 55% 8%, rgba(107,68,155,.55), transparent 70%),
      linear-gradient(180deg, #1d0c36 0%, var(--night) 45%, var(--ink) 100%);
    font-family: "Oswald", sans-serif; color: var(--white); text-align: center;
  }
  .stage-photo { position: absolute; left: 0; top: 0; width: 835px; height: 640px; }

  .brand { position: absolute; left: 53px; top: 22px; width: 340px; z-index: 2; }
  .brand-box { background: var(--slate); padding: 16px 18px 14px; text-align: center; }
  .brand-name {
    font-family: "Bebas Neue", sans-serif; font-size: 62px; line-height: .95;
    color: var(--white); letter-spacing: 1px;
  }
  .brand-tag {
    margin-top: 10px; font-family: "Oswald", sans-serif; font-weight: 500;
    font-size: 17px; letter-spacing: 8px; text-transform: uppercase; color: var(--white);
  }

  .headline {
    position: absolute; left: 0; right: 0; top: 455px;
    font-family: "Bebas Neue", sans-serif; font-weight: 400; font-size: 200px; line-height: .77;
    transform: scaleX(.74); transform-origin: center top;
    text-shadow: 0 0 34px rgba(255,255,255,.45);
  }
  .when {
    position: absolute; left: 0; right: 0; top: 762px;
    font-family: "Bebas Neue", sans-serif; font-size: 39px; line-height: 1; color: var(--lavender);
    text-shadow: 0 0 10px rgba(155,92,255,.8);
  }
  .band {
    position: absolute; left: 0; right: 0; top: 812px;
    font-family: "Bebas Neue", sans-serif; font-size: 29px; line-height: 1; color: var(--pink);
  }
  .ages {
    position: absolute; left: 0; right: 0; top: 870px;
    font-family: "Bebas Neue", sans-serif; font-size: 42px; line-height: 1;
  }
  .donate {
    position: absolute; left: 100px; right: 100px; top: 912px;
    font-size: 18px; line-height: 1.2; font-weight: 400;
  }
  .donate strong { font-weight: 600; }

  .artist {
    position: absolute; left: 160px; top: 958px;
    display: flex; align-items: center; gap: 14px; text-align: left;
  }
  .artist-photo { width: 100px; height: 82px; display: block; }
  .artist-label { font-family: "Bebas Neue", sans-serif; font-size: 22px; color: var(--pink); line-height: 1; }
  .artist-name { font-family: "Bebas Neue", sans-serif; font-size: 42px; color: var(--pink); line-height: .95; letter-spacing: 1px; }
  .artist-role { font-family: "Bebas Neue", sans-serif; font-size: 22px; color: var(--pink); line-height: 1; }

  .venue {
    position: absolute; left: 60px; right: 60px; top: 1050px;
    padding: 2px 0;
    background: linear-gradient(90deg, transparent, rgba(255,255,255,.08), transparent);
    font-family: "Cinzel", serif; font-weight: 600; font-size: 31px; letter-spacing: 5px; line-height: 1.15;
  }
  .address {
    position: absolute; left: 0; right: 0; top: 1094px;
    font-family: "Bebas Neue", sans-serif; font-size: 36px; line-height: 1; color: var(--pink); letter-spacing: 1px;
  }

  .footer { position: absolute; left: 0; right: 0; top: 1138px; height: 50px; }
  .partner { position: absolute; top: 4px; width: 40px; height: 40px; }
  .partner.one { left: 62px; background: var(--red); }
  .partner.two { left: 110px; background: var(--white); }
  .partner.three { left: 158px; background: var(--slate); }
  .info-bar {
    position: absolute; left: 200px; width: 428px; top: 2px; height: 44px;
    background: var(--pink); color: var(--white); padding-top: 4px;
  }
  .info-link { font-family: "Bebas Neue", sans-serif; font-size: 20px; line-height: 1; white-space: nowrap; }
  .info-credit { font-family: "Bebas Neue", sans-serif; font-size: 16px; line-height: 1.1; color: var(--night); white-space: nowrap; }
  .host-mark {
    position: absolute; left: 645px; top: 4px; width: 150px; height: 40px;
    display: flex; align-items: center; gap: 6px; font-size: 13px; font-weight: 500;
    text-align: left; line-height: 1.1; color: var(--white);
  }
  .host-mark .square { width: 14px; height: 14px; background: var(--white); flex: none; }
</style>
</head>
<body>
<main class="flyer">
  <svg class="stage-photo" viewBox="0 0 835 640" role="img" aria-label="Worship band performing with raised hands on a purple-lit stage">
    <defs>
      <linearGradient id="stageFill" x1="0" y1="0" x2="1" y2="1">
        <stop offset="0" stop-color="#2c0f57"/>
        <stop offset=".35" stop-color="#7a34d8"/>
        <stop offset=".6" stop-color="#b46cff"/>
        <stop offset="1" stop-color="#2a0e4a"/>
      </linearGradient>
      <radialGradient id="stageShade" cx=".5" cy=".5" r=".6">
        <stop offset="0" stop-color="#000" stop-opacity="0"/>
        <stop offset="1" stop-color="#0a0414" stop-opacity=".55"/>
      </radialGradient>
      <linearGradient id="upperFill" x1="0" y1="0" x2="0" y2="1">
        <stop offset="0" stop-color="#1a0a30"/>
        <stop offset="1" stop-color="#4a1d8a"/>
      </linearGradient>
    </defs>
    <polygon points="0,0 835,0 835,105 0,290" fill="url(#upperFill)" opacity=".7"/>
    <polygon points="0,290 835,105 835,520 0,590" fill="url(#stageFill)"/>
    <polygon points="0,290 835,105 835,520 0,590" fill="url(#stageShade)"/>
    <polygon points="0,286 835,101 835,107 0,292" fill="rgba(255,255,255,.3)"/>
  </svg>

  <header class="brand">
    <div class="brand-box">
      <div class="brand-name">Encounter G.L.O.</div>
    </div>
    <div class="brand-tag">Hour of Glory</div>
  </header>

  <h1 class="headline">Let's<br>Worship!</h1>
  <p class="when">Wednesday, May 27th, 2015 7:00 PM to 8:15 PM</p>
  <p class="band">Live band covering your favorite<br>popular contemporary Christian music!</p>
  <p class="ages">All ages welcome!</p>
  <p class="donate">Event is <strong>FREE</strong>!! Please bring a donation of gently used clothing<br>items or new toiletry item. <strong>Benefit for: The Open Hands Mission</strong></p>

  <section class="artist">
    <svg class="artist-photo" viewBox="0 0 100 82" role="img" aria-label="Portrait of debut artist Talia Verhoeven">
      <defs>
        <linearGradient id="artistFill" x1="0" y1="0" x2="0" y2="1">
          <stop offset="0" stop-color="#8fd0ee"/>
          <stop offset="1" stop-color="#2f6f9a"/>
        </linearGradient>
      </defs>
      <rect width="100" height="82" fill="url(#artistFill)"/>
    </svg>
    <div>
      <div class="artist-label">This month's debut artist:</div>
      <div class="artist-name">Talia Verhoeven</div>
      <div class="artist-role">Local Christian Singer/Songwriter</div>
    </div>
  </section>

  <p class="venue">THE HARBORVIEW CHAPEL</p>
  <p class="address">2715 W Maple Crest Rd; Fort Lauderdale, FL 33918</p>

  <footer class="footer">
    <span class="partner one"></span>
    <span class="partner two"></span>
    <span class="partner three"></span>
    <div class="info-bar">
      <div class="info-link">For more details, visit: www.encounterpraiseGLO.example</div>
      <div class="info-credit">Brought to you by: Delphine Marsh Music</div>
    </div>
    <div class="host-mark"><span class="square"></span>The Harborview Chapel</div>
  </footer>
</main>
</body>
</html>
```